Voice Over IP Service

Create a 1-2 page brochure for our voice over IP phone system service.

The color pallet should use these colors..
#e23232 red
#636466 Grey
#434445 Dark grey

```html
<!DOCTYPE html>
<html lang="en">
<head>
<meta charset="utf-8">
<title>Harborline Telecom – Hosted VOIP Phone Service</title>
<link rel="stylesheet" href="https://fonts.googleapis.com/css2?family=Roboto:wght@300;400&family=Roboto+Condensed:ital,wght@0,700;1,700&display=swap">
<style>
  :root {
    --red: #e23232;
    --grey: #636466;
    --dark-grey: #434445;
    --text: #2b2b2c;
    --paper: #ffffff;
  }
  * { margin: 0; padding: 0; box-sizing: border-box; }
  html, body { width: 927px; height: 1200px; overflow: hidden; background: var(--paper); }
  .page { position: relative; width: 927px; height: 1200px; font-family: "Roboto", sans-serif; color: var(--text); }

  .side-label { position: absolute; left: 65px; width: 120px; }
  .side-label svg { position: absolute; inset: 0; overflow: visible; }
  .side-label p {
    position: absolute; left: 0; right: 0; top: 50%; transform: translateY(-50%);
    text-align: center; font-family: "Roboto Condensed", sans-serif; font-style: italic; font-weight: 700;
    color: var(--red); font-size: 19px; line-height: 23.5px;
  }

  .rule { position: absolute; left: 206px; width: 655px; border-top: 1px dashed var(--red); opacity: .7; }

  .intro { position: absolute; left: 206px; top: 94px; width: 655px; font-size: 16.5px; line-height: 22px; }

  .features { position: absolute; left: 216px; top: 250px; width: 645px; list-style: none; }
  .feature { position: relative; padding-left: 28px; font-size: 15.6px; line-height: 20px; margin-bottom: 14px; }
  .feature h3 {
    font-family: "Roboto Condensed", sans-serif; font-weight: 700; font-size: 19px; line-height: 22px;
    color: var(--grey);
  }
  .arrow-icon { position: absolute; left: 0; top: 5px; width: 17px; height: 13px; }

  .services-lead {
    position: absolute; left: 246px; top: 783px;
    font-family: "Roboto Condensed", sans-serif; font-style: italic; font-weight: 700; font-size: 19px; color: var(--red);
  }
  .services { position: absolute; left: 497px; top: 732px; list-style: none; }
  .services li {
    position: relative; padding-left: 30px; height: 26px;
    font-family: "Roboto Condensed", sans-serif; font-weight: 700; font-size: 19px; line-height: 22px; color: var(--grey);
  }
  .services .arrow-icon { top: 5px; }

  .cta { position: absolute; left: 64px; top: 917px; width: 797px; height: 177px; background: var(--red); }
  .cta svg { position: absolute; inset: 0; }
  .cta p {
    position: absolute; left: 0; right: 0; top: 38px; text-align: center;
    color: #fff; font-size: 30px; line-height: 36.5px; font-weight: 400;
  }
  .cta .light { font-weight: 300; }

  .footer { position: absolute; left: 80px; top: 1114px; width: 781px; height: 46px; }
  .brand { position: absolute; left: 0; top: 6px; display: flex; align-items: center; gap: 8px; }
  .brand-mark { width: 30px; height: 30px; border: 2.5px solid var(--red); border-radius: 5px; }
  .brand-name { font-family: "Roboto", sans-serif; font-weight: 400; font-size: 27px; color: var(--dark-grey); letter-spacing: -.5px; }
  .address { position: absolute; left: 256px; top: 0; font-size: 15.3px; line-height: 20px; color: var(--grey); }
  .address .key { color: var(--red); }
</style>
</head>
<body>
<div class="page">

  <!-- Section 1 -->
  <div class="rule" style="top:59px"></div>
  <div class="side-label" style="top:58px;height:142px">
    <svg width="120" height="142" viewBox="0 0 120 142" fill="none" stroke="#e23232" stroke-width="1.3">
      <path d="M1 1H114M1 1V124M117 14V141H6"/>
      <path d="M120 1l-7-3v6z M1 141l7-3v6z" fill="#e23232" stroke="none"/>
    </svg>
    <p>Why<br>Choose<br>Our Hosted<br>VOIP Phone<br>Service?</p>
  </div>
  <p class="intro">At Harborline Telecom our business phone service is best-of-breed that utilizes redundant servers in geographically disperse regions throughout the country to ensure high reliability and sound quality.</p>

  <!-- Section 2 -->
  <div class="rule" style="top:237px"></div>
  <div class="side-label" style="top:236px;height:142px">
    <svg width="120" height="142" viewBox="0 0 120 142" fill="none" stroke="#e23232" stroke-width="1.3">
      <path d="M1 1H114M1 1V124M117 14V141H6"/>
      <path d="M120 1l-7-3v6z M1 141l7-3v6z" fill="#e23232" stroke="none"/>
    </svg>
    <p>Additionally,<br>people<br>appreciate<br>the<br>following…</p>
  </div>

  <ul class="features">
    <li class="feature">
      <svg class="arrow-icon" viewBox="0 0 17 13"><path d="M0 5h10V0l7 6.5L10 13V8H0z" fill="#636466"/></svg>
      <h3>Competitive pricing:</h3>
      Low flat-fee pricing for unlimited local and long-distance phone service. Our pricing includes an extensive feature list that includes routing by time-frames, easy to create work-flows, company greeting and menu-list (Auto Attendant), ring-all or find the available staff member, call-center reporting and more.
    </li>
    <li class="feature">
      <svg class="arrow-icon" viewBox="0 0 17 13"><path d="M0 5h10V0l7 6.5L10 13V8H0z" fill="#636466"/></svg>
      <h3>No set-up fees!</h3>
      Let us do the heavy-lifting. We will plan and configure your dream phone system as part of our service.
    </li>
    <li class="feature">
      <svg class="arrow-icon" viewBox="0 0 17 13"><path d="M0 5h10V0l7 6.5L10 13V8H0z" fill="#636466"/></svg>
      <h3>Quality phones</h3>
      We include business phones by Norvell and we support most VOIP phone manufacturers including Kestra, Norvell, Aurion, Tellmark and many others.
    </li>
    <li class="feature">
      <svg class="arrow-icon" viewBox="0 0 17 13"><path d="M0 5h10V0l7 6.5L10 13V8H0z" fill="#636466"/></svg>
      <h3>Call Center</h3>
      Track stats on call-center flow, abandoned calls, voicemails, hold times, and more. Our granular reports and call center manager portal allow you to manage your team better than ever.
    </li>
    <li class="feature">
      <svg class="arrow-icon" viewBox="0 0 17 13"><path d="M0 5h10V0l7 6.5L10 13V8H0z" fill="#636466"/></svg>
      <h3>Audio &amp; Video Conferencing</h3>
      Audio conferencing and video conferencing are a rising need for modern business. Remove the need for multiple applications and handle all client communication under one platform.
    </li>
  </ul>

  <!-- Section 3 -->
  <div class="rule" style="top:720px"></div>
  <div class="side-label" style="top:720px;height:142px">
    <svg width="120" height="142" viewBox="0 0 120 142" fill="none" stroke="#e23232" stroke-width="1.3">
      <path d="M1 1H114M1 1V124M117 14V141H6"/>
      <path d="M120 1l-7-3v6z M1 141l7-3v6z" fill="#e23232" stroke="none"/>
    </svg>
    <p>We are a<br>full-service<br>VOIP phone<br>system<br>vendor.</p>
  </div>
  <p class="services-lead">Our services include…</p>
  <ul class="services">
    <li><svg class="arrow-icon" viewBox="0 0 17 13"><path d="M0 5h10V0l7 6.5L10 13V8H0z" fill="#636466"/></svg>Planning</li>
    <li><svg class="arrow-icon" viewBox="0 0 17 13"><path d="M0 5h10V0l7 6.5L10 13V8H0z" fill="#636466"/></svg>Phone sales</li>
    <li><svg class="arrow-icon" viewBox="0 0 17 13"><path d="M0 5h10V0l7 6.5L10 13V8H0z" fill="#636466"/></svg>Installation</li>
    <li><svg class="arrow-icon" viewBox="0 0 17 13"><path d="M0 5h10V0l7 6.5L10 13V8H0z" fill="#636466"/></svg>Support</li>
    <li><svg class="arrow-icon" viewBox="0 0 17 13"><path d="M0 5h10V0l7 6.5L10 13V8H0z" fill="#636466"/></svg>Management</li>
  </ul>

  <!-- Call to action -->
  <div class="cta">
    <svg width="797" height="177" viewBox="0 0 797 177" fill="none" stroke="#fff" stroke-width="1.6">
      <path d="M28 23H778M28 23V133M773 35V155H44"/>
      <path d="M784 23l-9-4v8z M36 155l9-4v8z" fill="#fff" stroke="none"/>
    </svg>
    <p>Call us direct at <span class="light">555-201-4870</span> to get<br>a <span class="light">FREE</span> consultation or demonstration<br>with absolutely no pressure or obligation.</p>
  </div>

  <!-- Footer -->
  <footer class="footer">
    <div class="brand">
      <span class="brand-mark"></span>
      <span class="brand-name">Harborline</span>
    </div>
    <p class="address">Harborline Telecom 1820 Meridian Way Bayport, VA 23999<br>
      <span class="key">TF</span> 800-555-0142 <span class="key">PH</span> 555-201-3300 <span class="key">FX</span> 555-201-3311</p>
  </footer>

</div>
</body>
</html>
```